Sports Performance Facility Grand Opening

I am planning the grand opening of my new training facility. We are moving and expanding. We specialize in training athletes of all ages and now will offer facility rentals. We will offer team training, group speed and agility training, baseball/softball academy, and our Football Academy. We would like to kick off our new Facility January 10th from 11:00-3:00pm. We will offer premium training packages and special facility rental rates at the opening. Along with this, if a team contacts us before the opening and mentions the post card, they will receive a special offer to rent the facility. We are going to relocate to 42 Corvell St just off I78 and conveniently located in the Lehigh Valley. We want to signify that we will provide elite training programs at a premium. Along with this, our facility rentals provide a unique opportunity for us to have a one stop shop for all our clients individual and team training needs. We are excited to get back into the Lehigh Valley and continue working with the Valley's premier teams and athletes. Provide tel #610.482.9067 and email. Marcus@marcuselwinpeak.com

Target Market(s)

We are targeting athletes ranging from youth levels to the professionals. youth, travel, and high school teams to rent our facility. Adults looking to workout like an athlete.

Industry/Entity Type

Training

Requirements
Must have
• Grand Opening and Special Offer/ Contact us to reserve our facility today.
Nice to have
• Be creative and create an idea that would cause people to bring friends/coaches/ etc...to receive additional program savings
Should not have
• Clip art that is old and outdated.

```html
<!DOCTYPE html>
<html lang="en">
<head>
<meta charset="utf-8">
<title>Peak Training – Grand Opening Postcard</title>
<link rel="stylesheet" href="https://fonts.googleapis.com/css2?family=Arimo:wght@400;700&display=swap">
<style>
  :root {
    --backdrop: #5a3a26;
    --card-red: #e8323a;
    --ink: #262320;
    --accent-red: #e0323a;
    --white: #ffffff;
    --photo-light: #f2eee4;
    --photo-mid: #c9a77a;
    --photo-dark: #2b2240;
    --dots: rgba(255,255,255,0.85);
  }
  * { margin: 0; padding: 0; box-sizing: border-box; }
  html, body {
    width: 1200px; height: 601px; overflow: hidden;
    background: var(--backdrop);
    font-family: "Arimo", Arial, sans-serif;
  }
  .postcard {
    position: absolute; left: 95px; top: 105px;
    width: 1010px; height: 388px;
    display: flex;
  }
  .postcard__front {
    position: relative; width: 505px; height: 100%; overflow: hidden;
  }
  .front__photo {
    position: absolute; inset: 0;
    background:
      radial-gradient(ellipse 180px 260px at 400px 180px, rgba(70,130,190,0.55), transparent 70%),
      radial-gradient(ellipse 200px 120px at 330px 330px, rgba(230,170,60,0.45), transparent 70%),
      linear-gradient(175deg, var(--photo-light) 0%, var(--photo-light) 45%, var(--photo-mid) 68%, var(--photo-dark) 88%);
  }
  .front__copy {
    position: absolute; left: 27px; top: 32px;
    font-size: 10.4px; line-height: 15px; color: var(--ink);
    white-space: nowrap;
  }
  .front__copy strong { font-weight: 700; }
  .front__copy .highlight { color: var(--accent-red); font-weight: 700; }
  .brand {
    position: absolute; left: 28px; top: 302px;
  }
  .brand__name {
    font-size: 36px; font-weight: 700; color: var(--white);
    letter-spacing: 1px; line-height: 36px;
  }
  .brand__tagline {
    margin-top: 14px; font-size: 7px; font-weight: 700; color: var(--white);
  }
  .contact {
    position: absolute; left: 30px; top: 363px;
    font-size: 11px; color: var(--white);
  }
  .postcard__back {
    position: relative; width: 505px; height: 100%;
    background: var(--card-red);
  }
  .back__promo {
    position: absolute; left: 26px; top: 62px; width: 205px;
    color: var(--white);
  }
  .promo__headline {
    font-size: 34px; font-weight: 700; line-height: 36px;
    letter-spacing: 0.5px; text-transform: uppercase;
  }
  .promo__date {
    margin-top: 14px; font-size: 13px; font-weight: 700; line-height: 18px;
  }
  .promo__rule {
    width: 48px; height: 3px; margin: 18px 0; background: var(--white);
  }
  .promo__offer {
    font-size: 12px; line-height: 17px;
  }
  .promo__cta {
    margin-top: 16px; font-size: 15px; font-weight: 700; line-height: 20px;
  }
  .back__divider {
    position: absolute; left: 251px; top: 53px; height: 280px;
    border-left: 1px dotted var(--dots);
  }
  .back__address-lines {
    position: absolute; left: 267px; top: 146px; width: 210px;
  }
  .back__address-lines span {
    display: block; height: 33px;
    border-top: 1px dotted var(--dots);
  }
</style>
</head>
<body>
  <article class="postcard">
    <section class="postcard__front">
      <div class="front__photo" role="img" aria-label="Action photo of a female sprinter bursting forward amid colourful paint splashes"></div>
      <p class="front__copy">
        We are moving and expanding. We specialize in<br>
        training athletes of all ages and now will offer facility<br>
        rentals. We will offer team training, group speed and<br>
        agility training, baseball/softball academy, and our Football<br>
        Academy. We would like to kick off our new Facility <span class="highlight">January</span><br>
        <span class="highlight">10th from 11:00-3:00pm</span>. We will offer premium training<br>
        packages and special facility rental rates at the opening. Along<br>
        with this, if a team contacts us before the opening and mentions<br>
        the post card, they will receive a special offer to rent the facility.<br>
        We are going to relocate to <strong>42 Corvell St</strong> just off I78 and conveniently located in the<br>
        Lehigh Valley. We want to signify that we will provide elite training programs at a<br>
        premium. Along with this, our facility rentals provide a unique opportunity for us<br>
        to have a one stop shop for all our clients individual and team training needs.<br>
        We are excited to get back into the Lehigh Valley and continue working<br>
        with the Valley's premier teams and athletes.
      </p>
      <div class="brand">
        <div class="brand__name">PEAK</div>
        <div class="brand__tagline">Speed · Strength · Agility · Training</div>
      </div>
      <p class="contact">Tel #610.482.9067 and email:Marcus@marcuselwinpeak.com</p>
    </section>
    <section class="postcard__back">
      <div class="back__promo">
        <h1 class="promo__headline">Grand<br>Opening</h1>
        <p class="promo__date">January 10th<br>11:00–3:00pm</p>
        <div class="promo__rule"></div>
        <p class="promo__offer">Special Offer: premium training packages and facility rental rates.</p>
        <p class="promo__cta">Contact us to reserve our facility today.</p>
      </div>
      <div class="back__divider"></div>
      <div class="back__address-lines">
        <span></span><span></span><span></span><span></span><span></span><span></span>
      </div>
    </section>
  </article>
</body>
</html>
```